・大阪らしい闊達で明るいイメージ
・2025年開催予定のひかり環境博覧祭に向けて変わっていく新しい大阪のイメージ
・一目で南学競のパンフレットとわかるようなデザイン
・コロナ禍からの復活の象徴となる、ハンパなく熱い大会を彷彿とさせるデザイン
にしたいと思ってます。オリジナル・未発表の作品でお願い致します。

また、記載項目といたしまして
・表紙には以下の4項目を必ず記載してください。
1. 燃えまくり!!南学競
※阪には「はん」と上にふりがなをつけてください
※ぇは小さい「え」です
2. 開催日程:2023年7月31日(月)~8月25日(金)
3. 第75回南部医療学徒連合競技祭
4. 代表主管校:緑丘学院大学
・裏表紙には以下の2項目を必ず記載してください。
1. 〒999-0412 大阪府吹田市桜野台9丁目4 緑丘学院大学第75回南学競運営室
2. 第75回南部医療学徒連合競技祭運営委員会
B5
4ページ
• イラストレーター形式 (.ai)
・ページ数は4ページとしておりますが、デザインがそろっていれば何ページでも構いません。
・イラストはイラストレーター形式にて縦長仕様でお願いします。
・そのまま印刷会社に入稿するので、カラーモードはCMYKにて、塗り足し・アウトライン化もお願いします。
・ご提案を選択後、当選者様に修正を依頼する可能性がございますのでご了承ください。
・選択させていただいたデザインの著作権(財産権)等の扱いはDraftora利用規約に従い、弊運営委員会への譲渡をお願いします。
・以下に過去大会の総合パンフレットデザインを添付いたします。
・その他、何かご不明な点などございましたら、お気軽にご相談ください。
第72回、70回南学競のパンフレットデザインを添付いたします。

・「燃えまくり!!南学競」のスローガンに合う明るく勢いのあるデザイン
・一目で体育大会のポスターだとわかるデザイン
・星影の柱は緑丘学院大学(吹田キャンパス)の近くにあり、主管校の地域を反映したデザインになっている
・ポスター、パンフレットの表紙にふさわしい、シンプルながらも目をひくデザイン
・修正の依頼にもご丁寧に対応していただき、よりよいデザインに仕上げてくださった

以上の点からぴの様のデザインを選ばせていただきました。

たくさんのご応募をいただき、心より感謝申し上げます。
当選作品を選ぶのが非常に困難でしたが、どれも素晴らしいデザインでした。
来年も南学競のポスター・パンフレットデザインを募集することがあるかもしれません。
その際は、ぜひまたみなさまのご応募をお待ちしております。

今回のご参加、そして素晴らしい作品をご提案していただき、誠にありがとうございました。

```html
<!DOCTYPE html>
<html lang="ja">
<head>
<meta charset="utf-8">
<title>燃えまくり!!南学競 第75回南部医療学徒連合競技祭</title>
<link rel="stylesheet" href="https://fonts.googleapis.com/css2?family=Noto+Sans+JP:wght@500;700;900&family=Oswald:wght@500;700&display=swap">
<style>
  :root {
    --paper: #ffffff;
    --ink: #1a1a1a;
    --red: #e0191f;
    --grey: #b9b9b9;
    --grey-soft: #dcdcdc;
    --blue: #2f74c8;
    --skin-light: #f4d9c8;
    --skin-mid: #e4b7a0;
  }
  html, body {
    margin: 0;
    padding: 0;
    overflow: hidden;
    background: var(--paper);
  }
  .poster {
    position: relative;
    width: 848px;
    height: 1200px;
    overflow: hidden;
    background: var(--paper);
    font-family: "Noto Sans JP", sans-serif;
    color: var(--ink);
  }
  .hero-photo {
    position: absolute;
    left: 0;
    top: 0;
    width: 600px;
    height: 1200px;
    background:
      radial-gradient(ellipse 70% 50% at 25% 35%, var(--skin-mid) 0%, var(--skin-light) 45%, rgba(244,217,200,0.45) 72%, rgba(255,255,255,0) 100%);
  }
  .echo {
    position: absolute;
    right: 36px;
    top: 18px;
    text-align: right;
    font-weight: 900;
    line-height: 1.08;
  }
  .echo span { display: block; }
  .echo .e1 { font-size: 24px; color: var(--grey-soft); }
  .echo .e2 { font-size: 30px; color: var(--grey-soft); }
  .echo .e3 { font-size: 40px; color: var(--grey-soft); }
  .echo .e4 { font-size: 56px; color: var(--grey); }
  .echo .e5 { font-size: 70px; color: var(--grey); }
  .edition {
    position: absolute;
    left: 520px;
    top: 466px;
    display: flex;
    align-items: center;
    gap: 12px;
  }
  .edition-name {
    font-family: "Oswald", sans-serif;
    font-weight: 700;
    font-size: 15px;
    line-height: 1.15;
    font-style: italic;
  }
  .edition-number {
    font-family: "Oswald", sans-serif;
    font-weight: 700;
    font-size: 42px;
    line-height: 1;
    color: var(--red);
    font-style: italic;
  }
  .edition-number small { font-size: 26px; }
  .ruby-call {
    position: absolute;
    left: 138px;
    top: 462px;
    font-size: 48px;
    font-weight: 900;
    line-height: 1;
    color: var(--red);
    transform: rotate(-6deg);
  }
  .slogan {
    position: absolute;
    left: 150px;
    top: 536px;
    margin: 0;
    font-size: 96px;
    font-weight: 900;
    color: var(--red);
    letter-spacing: -4px;
    line-height: 1.1;
    white-space: nowrap;
  }
  .event-short {
    position: absolute;
    left: 96px;
    top: 672px;
    font-size: 212px;
    font-weight: 900;
    line-height: 1;
    letter-spacing: -2px;
  }
  .year {
    position: absolute;
    right: 32px;
    top: 868px;
    font-family: "Oswald", sans-serif;
    font-weight: 700;
    font-size: 30px;
    line-height: 1;
    color: var(--blue);
  }
  .event-full {
    position: absolute;
    left: 90px;
    top: 918px;
    font-weight: 900;
    line-height: 1.3;
  }
  .event-full .line1 { font-size: 24px; display: block; }
  .event-full .line2 { font-size: 46px; display: block; letter-spacing: 2px; }
  .dates {
    position: absolute;
    left: 410px;
    top: 908px;
    display: flex;
    align-items: flex-start;
    gap: 10px;
    color: var(--red);
    font-family: "Oswald", sans-serif;
    font-weight: 700;
  }
  .date { display: flex; flex-direction: column; align-items: flex-end; }
  .date b { font-size: 92px; line-height: 1; font-weight: 700; }
  .date i { font-style: normal; font-size: 11px; color: var(--ink); letter-spacing: 1px; }
  .dates svg { margin-top: 36px; }
  .host {
    position: absolute;
    right: 30px;
    bottom: 28px;
    font-size: 12px;
    font-weight: 500;
  }
</style>
</head>
<body>
  <main class="poster">
    <div class="hero-photo" role="img" aria-label="大声で泣き叫ぶ赤ちゃんのクローズアップ写真"></div>

    <div class="echo" aria-hidden="true">
      <span class="e1">燃えまくり!!</span>
      <span class="e2">燃えまくり!!</span>
      <span class="e3">燃えまくり!!</span>
      <span class="e4">燃えまくり!!</span>
      <span class="e5">燃えまくり!!</span>
    </div>

    <div class="edition">
      <div class="edition-name">South Medical Students<br>Games</div>
      <div class="edition-number">75<small>th</small></div>
    </div>

    <div class="ruby-call">はんっ</div>
    <h1 class="slogan">燃えまくり!!</h1>
    <div class="event-short">南学競</div>
    <div class="year">2023</div>

    <div class="event-full">
      <span class="line1">第75回 南部医療学徒</span>
      <span class="line2">連合競技祭</span>
    </div>

    <div class="dates">
      <div class="date"><b>7/31</b><i>MONDAY</i></div>
      <svg width="26" height="30" viewBox="0 0 30 34" aria-hidden="true">
        <polygon points="3,3 27,17 3,31" fill="none" stroke="var(--red)" stroke-width="4" stroke-linejoin="round"/>
      </svg>
      <div class="date"><b>8/25</b><i>FRIDAY</i></div>
    </div>

    <div class="host">代表主管校:緑丘学院大学</div>
  </main>
</body>
</html>
```